Lanterne architecture business cards

We are a new company based in New Zealand. We Specialize in High end Luxury Residential Architecture.

Every home is bespoke and is designed to each clients individual requirements and needs.

I like to design buildings that inspire people through light and form while offering a high level of comfort and usability.

Lines of sight, proportion and balance are fundamental to the spaces I create.
Updates

August 5th is current deadline - Today's date is the 13th of August.

Target Market(s)

New Zealanders who want a custom individual home design, typically 30-65 year old males and females

Industry/Entity Type

Architecture

Contact Information for Business Card

Director - Derek Tolson
Contact Number - 0279164073
Email - info@lanternearchitecture-example.co.nz
Webstie - www.lanternearchitecture-example.co.nz
Social Media - @lanternearchitecture

Font styles to use
Sans Serif

Requirements
Must have
• Logo (Both Sides)
Website
Email
Contact Number
Social Media

Nice to have
• Texture
Should not have
• More than 3 colours - typically I would've thought 2 would be good to match the logo.

```html
<!DOCTYPE html>
<html lang="en">
<head>
<meta charset="utf-8">
<title>Lanterne architecture — business cards</title>
<link rel="stylesheet" href="https://fonts.googleapis.com/css2?family=Jost:wght@400;500;600&display=swap">
<style>
  :root {
    --stage: #2b2b2b;
    --card-black: #070707;
    --gold-light: #f3e6a0;
    --gold-mid: #d9bf5c;
    --gold-deep: #a9862a;
    --gold-line: #c9a63c;
    --ink: #1b1a16;
    --logo-white: #f2f2f2;
  }
  html, body {
    margin: 0;
    width: 1200px;
    height: 900px;
    overflow: hidden;
    background: var(--stage);
    font-family: "Jost", "Helvetica Neue", Arial, sans-serif;
  }
  .card {
    position: absolute;
    left: 250px;
    width: 700px;
    height: 400px;
    border-radius: 40px;
    background: var(--card-black);
    overflow: hidden;
    box-shadow: 0 14px 30px rgba(0,0,0,0.45);
  }
  .card--front { top: 40px; }
  .card--back { top: 470px; }

  .front-frame {
    position: absolute;
    inset: 18px;
    border: 2px solid var(--gold-line);
    border-radius: 30px;
  }
  .wordmark {
    position: absolute;
    color: var(--logo-white);
    font-weight: 400;
    text-transform: uppercase;
    text-align: center;
    line-height: 1;
  }
  .wordmark__name {
    display: block;
    font-size: 34px;
    letter-spacing: 14px;
  }
  .wordmark__sub {
    display: block;
    font-size: 10px;
    letter-spacing: 16px;
    margin-top: 10px;
  }
  .card--front .wordmark {
    left: 0; right: 0;
    top: 172px;
  }
  .card--back .wordmark {
    left: 300px;
    width: 360px;
    top: 70px;
  }
  .card--back .wordmark__name { font-size: 28px; letter-spacing: 11px; }
  .card--back .wordmark__sub { font-size: 9px; letter-spacing: 12px; }

  .wave { position: absolute; inset: 0; }

  .contact {
    position: absolute;
    left: 58px;
    top: 238px;
    color: var(--ink);
  }
  .contact__name {
    margin: 0 0 12px;
    font-size: 24px;
    font-weight: 600;
    letter-spacing: 0.5px;
    text-transform: uppercase;
  }
  .contact__list { list-style: none; margin: 0; padding: 0; }
  .contact__item {
    display: flex;
    align-items: center;
    gap: 10px;
    font-size: 17px;
    font-weight: 400;
    margin-bottom: 6px;
  }
  .contact__item svg { width: 15px; height: 15px; flex: none; }

  .social {
    position: absolute;
    right: 46px;
    top: 196px;
    text-align: right;
    color: var(--ink);
  }
  .social__icons { display: flex; justify-content: flex-end; gap: 6px; margin-bottom: 8px; }
  .social__icon { width: 16px; height: 16px; background: var(--ink); border-radius: 3px; }
  .social__handle { font-size: 18px; font-weight: 400; }
</style>
</head>
<body>

<section class="card card--front" aria-label="Card front">
  <div class="front-frame"></div>
  <div class="wordmark">
    <span class="wordmark__name">Lanterne</span>
    <span class="wordmark__sub">Architecture</span>
  </div>
</section>

<section class="card card--back" aria-label="Card back">
  <svg class="wave" viewBox="0 0 700 400" preserveAspectRatio="none" aria-hidden="true">
    <defs>
      <linearGradient id="goldSweep" x1="0" y1="1" x2="1" y2="0">
        <stop offset="0" stop-color="#b8962f"/>
        <stop offset="0.35" stop-color="#f3e6a0"/>
        <stop offset="0.7" stop-color="#dcc264"/>
        <stop offset="1" stop-color="#a9862a"/>
      </linearGradient>
      <linearGradient id="goldEdge" x1="0" y1="0" x2="1" y2="0">
        <stop offset="0" stop-color="#a9862a"/>
        <stop offset="0.6" stop-color="#f3e6a0"/>
        <stop offset="1" stop-color="#c9a63c"/>
      </linearGradient>
    </defs>
    <path d="M380,196 C520,186 630,140 700,40 L700,70 C630,160 520,200 380,203 Z" fill="url(#goldEdge)"/>
    <path d="M0,400 L0,262 C90,216 200,206 330,206 C470,206 600,172 700,96 L700,400 Z" fill="url(#goldSweep)"/>
    <path d="M0,262 C90,216 200,206 330,206 C470,206 600,172 700,96 L700,104 C600,180 470,214 330,214 C200,214 90,224 0,270 Z" fill="#8f6f1e" opacity="0.55"/>
  </svg>

  <div class="wordmark">
    <span class="wordmark__name">Lanterne</span>
    <span class="wordmark__sub">Architecture</span>
  </div>

  <div class="social">
    <div class="social__icons">
      <span class="social__icon"></span>
      <span class="social__icon"></span>
      <span class="social__icon"></span>
    </div>
    <div class="social__handle">@lanternearchitecture</div>
  </div>

  <div class="contact">
    <h1 class="contact__name">Derek Tolson</h1>
    <ul class="contact__list">
      <li class="contact__item">
        <svg viewBox="0 0 16 16" aria-hidden="true"><rect x="4" y="1" width="8" height="14" rx="1.5" fill="none" stroke="#1b1a16" stroke-width="1.5"/><circle cx="8" cy="12.5" r="0.9" fill="#1b1a16"/></svg>
        0279164073
      </li>
      <li class="contact__item">
        <svg viewBox="0 0 16 16" aria-hidden="true"><rect x="1" y="3.5" width="14" height="9" rx="1" fill="#1b1a16"/><path d="M1.5 4 L8 9 L14.5 4" fill="none" stroke="#e8d58a" stroke-width="1.2"/></svg>
        info@lanternearchitecture-example.co.nz
      </li>
      <li class="contact__item">
        <svg viewBox="0 0 16 16" aria-hidden="true"><circle cx="8" cy="8" r="6.5" fill="none" stroke="#1b1a16" stroke-width="1.4"/><ellipse cx="8" cy="8" rx="2.8" ry="6.5" fill="none" stroke="#1b1a16" stroke-width="1.2"/><path d="M1.5 8 H14.5" stroke="#1b1a16" stroke-width="1.2"/></svg>
        www.lanternearchitecture-example.co.nz
      </li>
    </ul>
  </div>
</section>

</body>
</html>
```